BQL Groundworks & Freight Business Card

Can you please design a business card for an Earthworks, Haulage truck and machinery hire company. They also provide sand soil and mulch supply, as well as screening of products. Can you re-create the logo from the attached but add BQL Groundworks & Freight just use the three diamond design.

Target Market(s)

Earthmoving and Transport, Landscapers, Construction

Contact Information for Business Card

ABN 52 907 334 816, Doug Pelham, Managing Director, BQL Groundworks & Freight Mobile 0438 256 904 Email bqlfreight2010@mailvane.net

Font styles to use
Sans Serif

Colors
ec1f27
000000
cbcbcb
ffffff

Requirements
Must have
• Listed on the back, Earthworks | Haulage | Truck and Machinery Hire | Sand, Soil & Mulch Supply | Screening of Products
Nice to have
• Would be good for it to look appealing to a mans man, because it relates to heavy machinery, earthworks, construction etc. Black, red and white would be good maybe with a bit of silver somewhere.
Should not have
• not sure

```html
<!DOCTYPE html>
<html lang="en">
<head>
<meta charset="utf-8">
<title>BQL Groundworks &amp; Freight – Business Card</title>
<link href="https://fonts.googleapis.com/css2?family=Lato:wght@400;700;900&family=Roboto:wght@700&display=swap" rel="stylesheet">
<style>
  :root {
    --red: #ec1f27;
    --black: #000000;
    --silver: #cbcbcb;
    --white: #ffffff;
    --paper: #f4f4f4;
    --ink: #1a1a1a;
    --backdrop: #8d8d8d;
    --machine-yellow: #f2c230;
    --machine-amber: #e3a516;
  }
  * { margin: 0; padding: 0; box-sizing: border-box; }
  html, body { width: 1200px; height: 1200px; overflow: hidden; }
  body {
    position: relative;
    background: var(--backdrop);
    font-family: "Lato", Arial, sans-serif;
  }
  .card {
    position: absolute;
    border-radius: 16px;
    overflow: hidden;
  }
  /* Front */
  .card-front {
    left: 234px; top: 310px; width: 363px; height: 594px;
    background: var(--paper);
    color: var(--ink);
    text-align: center;
  }
  .brand-mark {
    position: absolute;
    left: 50%; top: 128px;
    width: 48px; height: 48px;
    margin-left: -24px;
    background: var(--red);
  }
  .brand-name {
    position: absolute;
    left: 0; right: 0; top: 212px;
    font-weight: 900;
    font-size: 23px;
    letter-spacing: 0.2px;
    color: var(--black);
  }
  .person-name {
    position: absolute; left: 0; right: 0; top: 327px;
    font-family: "Roboto", Arial, sans-serif;
    font-weight: 700;
    font-size: 29px;
    color: var(--red);
  }
  .person-role {
    position: absolute; left: 0; right: 0; top: 358px;
    font-size: 17px;
  }
  .contact-line {
    position: absolute; left: 0; right: 0;
    font-size: 17px;
  }
  .abn { top: 396px; }
  .abn-label { color: var(--red); }
  .phone { top: 432px; }
  .email { top: 455px; }
  .address-street { top: 492px; }
  .address-city { top: 514px; }

  /* Back */
  .card-back {
    left: 627px; top: 310px; width: 370px; height: 596px;
    background: var(--black);
  }
  .back-top {
    position: absolute; left: 0; top: 0; width: 100%; height: 348px;
    background: var(--red);
  }
  .machine-photo {
    position: absolute; left: 32px; top: 40px; width: 304px; height: 344px;
    border-radius: 6px;
    background: linear-gradient(160deg, var(--machine-yellow) 0%, var(--machine-amber) 70%, #2a2a2a 100%);
  }
  .services {
    position: absolute; left: 0; right: 0; top: 400px;
    list-style: none;
    text-align: center;
    color: var(--white);
    font-size: 17px;
    text-transform: uppercase;
    line-height: 31.3px;
  }
</style>
</head>
<body>
  <section class="card card-front" aria-label="Business card front">
    <div class="brand-mark"></div>
    <div class="brand-name">BQL GROUNDWORKS &amp; FREIGHT</div>
    <div class="person-name">DOUG PELHAM</div>
    <div class="person-role">Managing Director</div>
    <div class="contact-line abn"><span class="abn-label">ABN</span> 52 907 334 816</div>
    <div class="contact-line phone">0438 256 904</div>
    <div class="contact-line email">bqlfreight2010@mailvane.net</div>
    <div class="contact-line address-street">27 Corvell Way Marden 6031</div>
    <div class="contact-line address-city">Perth,WA</div>
  </section>

  <section class="card card-back" aria-label="Business card back">
    <div class="back-top"></div>
    <div class="machine-photo" role="img" aria-label="Photo of a yellow tracked excavator with its arm raised"></div>
    <ul class="services">
      <li>Earthworks</li>
      <li>Haulage</li>
      <li>Truck and Machinery Hire</li>
      <li>Sand, Soil &amp; Mulch Supply</li>
      <li>Screening of Products</li>
    </ul>
  </section>
</body>
</html>
```